Live Scavenger Hunt Mobile Platform needs a face lift!

We have been live for the past year and serving some very large customers, however, we are a group of developers that lack any real design skills. We are looking for a designer to help take our apps look and feel to the next level.

You can see the app in the Melodix store here: https://melodixstore.com/us/app/trekvo.co/id591327048?mt=8

And in fennel shelf here: https://fennelshelf.com/store/apps/developer?id=trekvoco&hl=en

We do not plan to change the UX of app, but rather just the aesthetics. Ideally, if this project works out well we would work with the same designer to update our site: http://trekvo.co

You can watch a video of how the platform works here:
http://clipnest.com/user3187254/elf-themed-christmas-scavenger-hunt

I have included the PSD files we used for the current mobile apps along with the PSD for our logo. In terms of colors we do like the current green and orange/red found in the logo. We have started to gravitate towards a brown textured background, but am open to change on this.

Requirements
Must have
• The home screen should have a larger focus on getting started vs. the other three categories of 'hunts, settings and help'. We worked with a Marlowbrook designer when re-skinning the app for the experience an we liked how they did this.

https://melodixstore.com/us/app/tiny-plum-quest/id836140572?mt=8
Nice to have
• - Custom web font (Some what playful) I am using Hobo Std in our logo
- Textured background
- Fun and playful, yet clean and clear. (Yes I realize that is a challenge)

```html
<!DOCTYPE html>
<html lang="en">
<head>
<meta charset="utf-8">
<title>trekvoco app screens</title>
<link href="https://fonts.googleapis.com/css2?family=PT+Sans+Narrow&family=Source+Sans+3:wght@400;600&display=swap" rel="stylesheet">
<style>
:root{
  --bar:#0f4b59;
  --bar-dark:#0a3a46;
  --ink:#15566a;
  --text:#555a5c;
  --muted:#8a8f91;
  --line:#d9dddd;
  --panel:#eeeeee;
  --select:#eef1e6;
  --accent:#d8481f;
  --white:#ffffff;
  --pill:#2b2a28;
}
*{box-sizing:border-box;margin:0;padding:0}
html,body{width:1200px;height:1000px;overflow:hidden;background:var(--white)}
body{font-family:"Source Sans 3",sans-serif;color:var(--text)}
.canvas{position:relative;width:1200px;height:1000px;overflow:hidden}
.abs{position:absolute}

.splash{left:0;top:35px;width:292px;height:455px;background:linear-gradient(180deg,#134f5d 0%,#2f5a4e 55%,#5a6a37 100%)}
.splash-brand{left:62px;top:145px;display:flex;align-items:center;gap:10px;color:#e9ecea;font-size:38px;font-weight:400}
.mark{width:22px;height:22px;background:var(--accent)}

.app-bar{height:56px;background:linear-gradient(180deg,var(--bar) 0%,var(--bar-dark) 100%)}
.bar-top{left:292px;top:35px;width:908px}
.bar-bottom{left:116px;top:530px;width:910px}
.brand{display:flex;align-items:center;gap:7px;color:var(--white);font-size:26px;font-weight:600;transform:translateX(-50%)}
.brand .mark{width:16px;height:16px}

.home{left:292px;top:91px;width:303px;height:399px;background:var(--panel)}
.start-card{left:306px;top:137px;width:274px;height:129px;background:var(--white);border:1px solid #c9cccc}
.map-art{left:312px;top:143px;width:134px;height:100px;background:linear-gradient(135deg,#b49a73,#7d6446)}
.start-label{left:463px;top:166px;font-family:"PT Sans Narrow",sans-serif;font-size:50px;color:var(--bar)}
.tile{top:304px;width:90px;height:90px;background:var(--white);border:1px solid #c9cccc;display:flex;flex-direction:column;align-items:center;justify-content:flex-end;padding-bottom:4px;font-family:"PT Sans Narrow",sans-serif;font-size:27px;color:var(--bar)}
.tile-icon{height:52px;display:flex;align-items:center;justify-content:center}
.runner{width:30px;height:48px;background:var(--bar);border-radius:14px}

.tabs{left:595px;top:91px;width:302px;height:37px;display:flex;border-bottom:1px solid var(--line)}
.tab{flex:1;display:flex;align-items:center;justify-content:center;font-size:19px;color:var(--ink)}
.tab.active{background:var(--bar);color:var(--white)}
.challenge{left:595px;width:302px;height:70px;border-bottom:1px solid var(--line);padding:13px 14px}
.challenge.selected{background:var(--select)}
.challenge h3{font-weight:400;font-size:19px;color:var(--ink)}
.challenge small{display:block;font-size:11px;color:var(--muted);margin-top:2px}
.chevron{position:absolute;right:8px;top:28px}
.score-tab{left:712px;top:463px;width:71px;height:26px;background:var(--pill);color:#e6e6e6;font-size:12px;border-radius:6px 6px 0 0;display:flex;align-items:center;justify-content:center}

.detail{left:913px;top:106px;width:264px}
.detail h2{font-weight:400;font-size:19px;color:var(--ink);margin-bottom:7px}
.detail p{font-size:15px;line-height:20px}
.detail .pts{font-size:13px;color:var(--muted);margin-top:9px}
.circle-btn{border:1px solid var(--ink);border-radius:50%;display:flex;align-items:center;justify-content:center;background:var(--white)}

.summary{left:137px;top:600px}
.summary-row{display:flex;height:35.5px;font-size:17px}
.summary-row dt{width:68px;color:var(--ink)}
.summary-row dd{font-size:15px;color:#444;padding-top:1px}
.resume{font-size:20px;color:var(--ink)}

.settings-label{left:440px;font-size:17px;color:var(--ink)}
.toggle{left:598px;top:615px;width:74px;height:26px;border:1px solid #b7bcbc;border-radius:13px;background:linear-gradient(#f4f4f4,#e2e2e2);font-size:14px;font-weight:600;color:#666;display:flex;align-items:center;padding-left:32px}
.toggle::before{content:"";position:absolute;left:2px;top:2px;width:21px;height:21px;border-radius:50%;background:var(--white);border:1px solid #bbb}
.text-field{left:562px;top:665px;width:147px;height:34px;border:1px solid var(--ink);background:var(--white)}
.sort-option{left:587px;font-size:15px;color:var(--muted)}

.help{left:742px;top:590px;width:256px}
.help h2{font-weight:400;font-size:19px;color:var(--ink);margin-bottom:9px}
.help p{font-size:12px;line-height:15.8px;color:#333;margin-bottom:21px}
</style>
</head>
<body>
<main class="canvas">

  <section class="abs splash">
    <div class="abs splash-brand"><span class="mark"></span>trekvo.co</div>
  </section>

  <header class="abs app-bar bar-top">
    <div class="abs brand" style="left:153px;top:12px"><span class="mark"></span>trekvoco</div>
    <svg class="abs" style="left:318px;top:16px" width="42" height="26" viewBox="0 0 42 26"><polygon points="0,13 15,0 15,7 42,7 42,19 15,19 15,26" fill="#fff"/></svg>
    <div class="abs brand" style="left:458px;top:12px"><span class="mark"></span>trekvoco</div>
    <svg class="abs" style="left:553px;top:13px" width="32" height="32" viewBox="0 0 32 32"><circle cx="16" cy="16" r="11" fill="none" stroke="#fff" stroke-width="7" stroke-dasharray="4.3 4.3"/><circle cx="16" cy="16" r="9" fill="#fff"/><circle cx="16" cy="16" r="4" fill="var(--bar)"/></svg>
    <svg class="abs" style="left:620px;top:16px" width="42" height="26" viewBox="0 0 42 26"><polygon points="0,13 15,0 15,7 42,7 42,19 15,19 15,26" fill="#fff"/></svg>
    <div class="abs brand" style="left:760px;top:12px"><span class="mark"></span>trekvoco</div>
    <svg class="abs" style="left:856px;top:13px" width="32" height="32" viewBox="0 0 32 32"><circle cx="16" cy="16" r="11" fill="none" stroke="#fff" stroke-width="7" stroke-dasharray="4.3 4.3"/><circle cx="16" cy="16" r="9" fill="#fff"/><circle cx="16" cy="16" r="4" fill="var(--bar)"/></svg>
  </header>

  <section class="abs home"></section>
  <div class="abs start-card"></div>
  <div class="abs map-art" role="img" aria-label="Folded world map with a compass"></div>
  <div class="abs start-label">Start</div>
  <div class="abs tile" style="left:307px">
    <div class="tile-icon" style="font-size:44px;line-height:1">?</div>Help
  </div>
  <div class="abs tile" style="left:397px">
    <div class="tile-icon"><div class="runner" role="img" aria-label="Running figure icon"></div></div>Hunts
  </div>
  <div class="abs tile" style="left:487px">
    <div class="tile-icon"><svg width="52" height="50" viewBox="0 0 52 50"><circle cx="22" cy="28" r="15" fill="none" stroke="var(--bar)" stroke-width="8" stroke-dasharray="5.2 5"/><circle cx="22" cy="28" r="12" fill="var(--bar)"/><circle cx="22" cy="28" r="5" fill="#fff"/><circle cx="42" cy="10" r="6" fill="none" stroke="var(--bar)" stroke-width="4" stroke-dasharray="2.6 2.4"/><circle cx="42" cy="10" r="3" fill="var(--bar)"/></svg></div>Settings
  </div>

  <nav class="abs tabs">
    <div class="tab active">Challenges</div>
    <div class="tab">Completed</div>
  </nav>
  <article class="abs challenge" style="top:128px"><h3>Challenge name</h3><small>10 point</small><svg class="chevron" width="10" height="14" viewBox="0 0 10 14"><polyline points="2,1 8,7 2,13" fill="none" stroke="var(--ink)" stroke-width="3"/></svg></article>
  <article class="abs challenge" style="top:198px"><h3>Challenge name</h3><small>10 point</small><svg class="chevron" width="10" height="14" viewBox="0 0 10 14"><polyline points="2,1 8,7 2,13" fill="none" stroke="var(--ink)" stroke-width="3"/></svg></article>
  <article class="abs challenge" style="top:268px"><h3>Challenge name</h3><small>&nbsp;point</small><svg class="chevron" width="10" height="14" viewBox="0 0 10 14"><polyline points="2,1 8,7 2,13" fill="none" stroke="var(--ink)" stroke-width="3"/></svg></article>
  <article class="abs challenge selected" style="top:338px"><h3>Challenge name</h3><small>10 point</small><svg class="chevron" width="10" height="14" viewBox="0 0 10 14"><polyline points="2,1 8,7 2,13" fill="none" stroke="var(--ink)" stroke-width="3"/></svg></article>
  <article class="abs challenge" style="top:408px"><h3>Challenge name</h3><small>10 point</small><svg class="chevron" width="10" height="14" viewBox="0 0 10 14"><polyline points="2,1 8,7 2,13" fill="none" stroke="var(--ink)" stroke-width="3"/></svg></article>
  <div class="abs score-tab">Score</div>

  <section class="abs detail">
    <h2>Name of the challenge</h2>
    <p>Now that we know who you are, I know who I am. I'm not a mistake! It all makes sense! In a comic, you know how you can tell who the arch-villain's going to be?</p>
    <p class="pts">10 points</p>
  </section>
  <div class="abs circle-btn" style="left:1003px;top:363px;width:91px;height:91px">
    <svg width="66" height="46" viewBox="0 0 66 46"><path d="M4 10h14l5-8h20l5 8h14a4 4 0 0 1 4 4v28a4 4 0 0 1-4 4H4a4 4 0 0 1-4-4V14a4 4 0 0 1 4-4z" fill="var(--bar)"/><rect x="50" y="4" width="9" height="5" fill="var(--bar)"/><circle cx="33" cy="27" r="13" fill="#fff"/><circle cx="33" cy="27" r="8" fill="var(--bar)"/></svg>
  </div>

  <header class="abs app-bar bar-bottom">
    <svg class="abs" style="left:20px;top:16px" width="38" height="24" viewBox="0 0 42 26"><polygon points="0,13 15,0 15,7 42,7 42,19 15,19 15,26" fill="#fff"/></svg>
    <div class="abs brand" style="left:155px;top:12px"><span class="mark"></span>trekvoco</div>
    <svg class="abs" style="left:252px;top:13px" width="32" height="32" viewBox="0 0 32 32"><circle cx="16" cy="16" r="11" fill="none" stroke="#fff" stroke-width="7" stroke-dasharray="4.3 4.3"/><circle cx="16" cy="16" r="9" fill="#fff"/><circle cx="16" cy="16" r="4" fill="var(--bar)"/></svg>
    <svg class="abs" style="left:322px;top:16px" width="38" height="24" viewBox="0 0 42 26"><polygon points="0,13 15,0 15,7 42,7 42,19 15,19 15,26" fill="#fff"/></svg>
    <div class="abs brand" style="left:458px;top:12px"><span class="mark"></span>trekvoco</div>
    <svg class="abs" style="left:554px;top:13px" width="32" height="32" viewBox="0 0 32 32"><circle cx="16" cy="16" r="11" fill="none" stroke="#fff" stroke-width="7" stroke-dasharray="4.3 4.3"/><circle cx="16" cy="16" r="9" fill="#fff"/><circle cx="16" cy="16" r="4" fill="var(--bar)"/></svg>
    <svg class="abs" style="left:625px;top:16px" width="38" height="24" viewBox="0 0 42 26"><polygon points="0,13 15,0 15,7 42,7 42,19 15,19 15,26" fill="#fff"/></svg>
    <div class="abs brand" style="left:762px;top:12px"><span class="mark"></span>trekvoco</div>
    <svg class="abs" style="left:858px;top:13px" width="32" height="32" viewBox="0 0 32 32"><circle cx="16" cy="16" r="11" fill="none" stroke="#fff" stroke-width="7" stroke-dasharray="4.3 4.3"/><circle cx="16" cy="16" r="9" fill="#fff"/><circle cx="16" cy="16" r="4" fill="var(--bar)"/></svg>
  </header>

  <dl class="abs summary">
    <div class="summary-row"><dt>Hunt:</dt><dd>hunt name</dd></div>
    <div class="summary-row"><dt>Date:</dt><dd>Nov. 19th 2011</dd></div>
    <div class="summary-row"><dt>Done:</dt><dd>5 of 50</dd></div>
    <div class="summary-row"><dt>Score:</dt><dd>37</dd></div>
    <div class="summary-row"><dt>Time:</dt><dd>Time is up!</dd></div>
  </dl>
  <div class="abs circle-btn resume" style="left:165px;top:858px;width:91px;height:91px">Resume</div>
  <div class="abs circle-btn" style="left:284px;top:857px;width:93px;height:93px">
    <svg width="66" height="46" viewBox="0 0 66 46"><path d="M4 10h14l5-8h20l5 8h14a4 4 0 0 1 4 4v28a4 4 0 0 1-4 4H4a4 4 0 0 1-4-4V14a4 4 0 0 1 4-4z" fill="var(--bar)"/><rect x="50" y="4" width="9" height="5" fill="var(--bar)"/><circle cx="33" cy="27" r="13" fill="#fff"/><circle cx="33" cy="27" r="8" fill="var(--bar)"/></svg>
  </div>

  <div class="abs settings-label" style="top:617px">Sound:</div>
  <div class="abs toggle">OFF</div>
  <div class="abs settings-label" style="top:672px">Team Name:</div>
  <div class="abs text-field"></div>
  <div class="abs settings-label" style="top:727px">Sort Points:</div>
  <div class="abs sort-option" style="top:728px">Low to High</div>
  <svg class="abs" style="left:680px;top:726px" width="22" height="18" viewBox="0 0 22 18"><polyline points="2,9 8,15 20,2" fill="none" stroke="var(--ink)" stroke-width="4"/></svg>
  <div class="abs sort-option" style="top:755px">High to Low</div>
  <div class="abs circle-btn" style="left:526px;top:859px;width:92px;height:92px">
    <svg width="58" height="56" viewBox="0 0 58 56"><path d="M0 0h48l10 10v46H0z" fill="var(--bar)"/><rect x="12" y="4" width="28" height="16" fill="#fff"/><rect x="30" y="6" width="7" height="12" fill="var(--bar)"/><rect x="8" y="30" width="42" height="22" fill="#fff"/></svg>
  </div>

  <section class="abs help">
    <h2>Hipster ipsum</h2>
    <p>Consectetur irure street art, lo-fi dreamcatcher butcher quinoa mlkshak. Perry dalton nisi odio Austin, odd fortune aesthetic vinyl pickled anim fugiat thunderkats master cleanse pour-over whatever keytar. Aute minim high life, helvetina cupidatat carles pinstack vinyl. Cillum ullamco ever semiotics. Loma brooklyn instant, marfa odd fortune before they sold out single-origin coffee aliqua semiotics.</p>
    <h2>Hipster ipsum</h2>
    <p>Vegan aesthetic qui, chambray pickled tumbler 8-bit direct trade ex assumenda blog readymade et fanny pack messenger bag. Leggings ex brooklyn, swag non locavore twee 8-bit authentic QRB cray nulla. Sriracha tempor wolf laboris DIY, wayfinders authentic accusamus cred kale chips occaecat scenester amber apparel esse. Sriracha non nulla, beard typewriter elit brunch hoodie anim labore bantly authentic gastropub. Carles williamsburg cobley sweater, cliche ullamco wolf fixie phablet tofu aliquip vinyl.</p>
  </section>

</main>
</body>
</html>
```